Tolvane Global Wordpress website design

We need a worddpress website/theme design for a new outsourcing company based in Australia.Name of the company is "Tolvane".
Website content is in progress.
The design needs to be clean without clutter in any section. Some example websites are provided below
Menu
- Resources
- Services
- Our difference
Home page needs to have a gif image, for example http://www.brindleworks.example. or http://www.corvathicket.example or http://www.corvathicket.example/team.html
We like how the corvathicket website flows without having the need to click on the menu. It is also mobile friendly (which is important)
Each piece of content will have a learn more button
A call to action button will be placed on the home page, which will provide our phone number and access to online form*
A call to action button will also be added to various other pages such as Resources.
Resources Section will contain web articles, whitepapers, blog and any other ccontent which helps customer in making a decision
Having the ability to add a video or images on the home page is also important
Ability to edit the content easily via wordpress is extremely important
* This is a great Contact Us form - http://www.pelgrastudio.example/#/schedule-meeting
* We do not need the traditional web form on the contact us page
Target Market(s)
Small to medium businesses requiring outsourcing services
Industry/Entity Type
It Company
Coding
Coded - Design and coding required
Colors
Designer to choose colors to be used in the design.
Look and feel
Each slider illustrates characteristics of the customer's brand and the style your logo design should communicate.

```html
<!DOCTYPE html>
<html lang="en">
<head>
<meta charset="utf-8">
<title>Tolvane Global – Website Screens</title>
<link href="https://fonts.googleapis.com/css2?family=Poppins:wght@400;500;600;700&display=swap" rel="stylesheet">
<style>
:root{
  --page:#eceef1;
  --white:#ffffff;
  --soft:rgba(255,255,255,.78);
  --line:rgba(255,255,255,.35);
  --red:#e5252c;
  --panel:#4a4c50;
  --panel-text:#c9cacc;
  --shade:rgba(18,22,30,.45);
}
*{margin:0;padding:0;box-sizing:border-box}
html,body{width:1200px;height:3727px;overflow:hidden}
body{background:var(--page);font-family:'Poppins',sans-serif;color:var(--white);position:relative}

.screen{position:absolute;left:169px;width:862px;height:465px;overflow:hidden}
.screen--hero-large{top:224px;width:837px;height:541px}
.screen--home{top:1125px}
.screen--services{top:1615px}
.screen--difference{top:2109px}
.screen--blog{top:2601px}
.screen--menu-open{top:3093px}

.photo{position:absolute;inset:0}
.photo::after{content:"";position:absolute;inset:0;background:linear-gradient(90deg,rgba(15,20,28,.55) 0%,rgba(15,20,28,.25) 55%,rgba(15,20,28,.35) 100%)}
.photo--meeting{background:linear-gradient(115deg,#6d7077 0%,#3b4450 35%,#2b4a7a 65%,#1f2b40 100%)}
.photo--service{background:linear-gradient(110deg,#5b4e44 0%,#7a6a5c 40%,#a99a88 70%,#6a5a4c 100%)}
.photo--team{background:linear-gradient(110deg,#3a3230 0%,#5c5a60 35%,#2e4a78 60%,#8a8f98 100%)}
.photo--reader{background:linear-gradient(110deg,#3c5a3a 0%,#6d7a66 35%,#5b5f68 60%,#3a3d44 100%)}

.site-header{position:absolute;top:24px;left:52px;right:42px;display:flex;align-items:center;z-index:2}
.brand{font-weight:500;font-size:22px;letter-spacing:5px;display:flex;align-items:center;gap:8px}
.brand-dot{width:8px;height:8px;background:var(--red)}
.header-tools{margin-left:auto;display:flex;align-items:center;gap:14px;font-size:8px}
.phone{display:flex;align-items:center;gap:5px;color:var(--soft)}
.btn-contact{border:1px solid var(--soft);padding:3px 12px;font-size:7px;letter-spacing:1px;text-transform:uppercase}
.burger{width:14px;display:flex;flex-direction:column;gap:3px}
.burger span{height:1px;background:var(--white)}

.hero{position:absolute;left:55px;top:150px;width:340px;z-index:2}
.screen--hero-large .hero{top:170px}
.tag{display:inline-block;background:var(--red);font-size:6px;font-weight:600;letter-spacing:.8px;text-transform:uppercase;padding:2px 7px;margin-bottom:6px}
.hero-title{font-weight:700;font-size:38px;line-height:1.1}
.hero-title--mid{font-size:26px;font-weight:600}
.hero-title--post{font-size:24px;font-weight:600;line-height:1.05}
.hero-text{font-size:8.5px;line-height:1.5;color:var(--soft);margin-top:12px;width:310px}
.byline{font-size:8px;color:var(--soft);margin-top:6px}
.btn-outline{display:inline-flex;align-items:center;gap:14px;margin-top:26px;border:1px solid var(--soft);padding:4px 10px;font-size:7px;letter-spacing:1px;text-transform:uppercase}
.btn-solid{display:inline-flex;align-items:center;gap:14px;margin-top:26px;background:var(--red);padding:5px 12px;font-size:7px;letter-spacing:1px;text-transform:uppercase}

.site-footer{position:absolute;left:52px;right:42px;bottom:14px;height:26px;border-top:1px solid var(--line);display:flex;align-items:flex-end;font-size:7.5px;color:var(--soft);z-index:2}
.follow{display:flex;align-items:center;gap:6px}
.social{width:7px;height:7px;border-radius:50%;background:var(--soft)}
.scroll{position:absolute;left:50%;transform:translateX(-50%);bottom:0;letter-spacing:1px;text-transform:uppercase;font-size:6.5px}
.footer-contact{margin-left:auto}

.menu-panel{position:absolute;top:0;right:0;width:220px;height:100%;background:var(--panel);padding:24px 30px;z-index:3;font-size:10px;font-weight:500;color:var(--panel-text)}
.menu-close{position:absolute;top:20px;right:28px;font-size:18px;font-weight:400;color:var(--white)}
.menu-list{list-style:none;display:flex;flex-direction:column;gap:16px}
.menu-list .current{color:var(--white);font-weight:600}
.submenu{list-style:none;margin:8px 0 0 10px;display:flex;flex-direction:column;gap:6px;font-size:8px;font-weight:400}
.submenu .active{color:var(--red)}
</style>
</head>
<body>

<!-- Home hero, tall format -->
<section class="screen screen--hero-large">
  <div class="photo photo--meeting" role="img" aria-label="Photo of colleagues in a business meeting, one resting his chin on his hand"></div>
  <header class="site-header">
    <div class="brand">TOLVANE</div>
    <div class="header-tools">
      <span class="phone"><svg width="8" height="8" viewBox="0 0 24 24"><path fill="#fff" d="M6.6 10.8a15 15 0 0 0 6.6 6.6l2.2-2.2a1 1 0 0 1 1-.25 11.4 11.4 0 0 0 3.6.6 1 1 0 0 1 1 1V20a1 1 0 0 1-1 1A17 17 0 0 1 3 4a1 1 0 0 1 1-1h3.5a1 1 0 0 1 1 1c0 1.25.2 2.45.6 3.6a1 1 0 0 1-.25 1z"/></svg>+1-202-555-0148</span>
      <span class="btn-contact">Contact Us</span>
      <span class="burger"><span></span><span></span><span></span></span>
    </div>
  </header>
  <div class="hero">
    <h1 class="hero-title">Welcome to<br>Tolvane</h1>
    <p class="hero-text">Lorem Ipsum is simply dummy text of the printing and typesetting industry. Lorem Ipsum has been the industry's standard dummy text ever printing and typesetting industry.</p>
    <span class="btn-outline">Our Story <svg width="8" height="8" viewBox="0 0 10 10"><path d="M2 8 8 2M4 2h4v4" stroke="#fff" fill="none"/></svg></span>
  </div>
  <footer class="site-footer">
    <div class="follow">Follow Us <span class="social"></span><span class="social"></span><span class="social"></span><span class="social"></span></div>
    <div class="scroll">Scroll Down</div>
    <div class="footer-contact">Contact Us</div>
  </footer>
</section>

<!-- Home -->
<section class="screen screen--home">
  <div class="photo photo--meeting" role="img" aria-label="Photo of colleagues in a business meeting"></div>
  <header class="site-header">
    <div class="brand">TOLVANE</div>
    <div class="header-tools">
      <span class="phone"><svg width="8" height="8" viewBox="0 0 24 24"><path fill="#fff" d="M6.6 10.8a15 15 0 0 0 6.6 6.6l2.2-2.2a1 1 0 0 1 1-.25 11.4 11.4 0 0 0 3.6.6 1 1 0 0 1 1 1V20a1 1 0 0 1-1 1A17 17 0 0 1 3 4a1 1 0 0 1 1-1h3.5a1 1 0 0 1 1 1c0 1.25.2 2.45.6 3.6a1 1 0 0 1-.25 1z"/></svg>+1-202-555-0148</span>
      <span class="btn-contact">Contact Us</span>
      <span class="burger"><span></span><span></span><span></span></span>
    </div>
  </header>
  <div class="hero">
    <h1 class="hero-title">Welcome to<br>Tolvane</h1>
    <p class="hero-text">Lorem Ipsum is simply dummy text of the printing and typesetting industry. Lorem Ipsum has been the industry's standard dummy text ever printing and typesetting industry.</p>
    <span class="btn-outline">Our Story <svg width="8" height="8" viewBox="0 0 10 10"><path d="M2 8 8 2M4 2h4v4" stroke="#fff" fill="none"/></svg></span>
  </div>
  <footer class="site-footer">
    <div class="follow">Follow Us <span class="social"></span><span class="social"></span><span class="social"></span><span class="social"></span></div>
    <div class="scroll">Scroll Down</div>
    <div class="footer-contact">Contact Us</div>
  </footer>
</section>

<!-- Services -->
<section class="screen screen--services">
  <div class="photo photo--service" role="img" aria-label="Photo of a smiling consultant and a client reviewing a tablet"></div>
  <header class="site-header">
    <div class="brand">TOLVANE</div>
    <div class="header-tools">
      <span class="phone"><svg width="8" height="8" viewBox="0 0 24 24"><path fill="#fff" d="M6.6 10.8a15 15 0 0 0 6.6 6.6l2.2-2.2a1 1 0 0 1 1-.25 11.4 11.4 0 0 0 3.6.6 1 1 0 0 1 1 1V20a1 1 0 0 1-1 1A17 17 0 0 1 3 4a1 1 0 0 1 1-1h3.5a1 1 0 0 1 1 1c0 1.25.2 2.45.6 3.6a1 1 0 0 1-.25 1z"/></svg>+1-202-555-0148</span>
      <span class="btn-contact">Contact Us</span>
      <span class="burger"><span></span><span></span><span></span></span>
    </div>
  </header>
  <div class="hero">
    <span class="tag">Services</span>
    <h2 class="hero-title hero-title--mid">Customer Experience</h2>
    <p class="hero-text">Lorem Ipsum is simply dummy text of the printing and typesetting industry. Lorem Ipsum has been the industry's standard dummy text ever printing and typesetting industry.</p>
    <span class="btn-solid">Explore <svg width="8" height="8" viewBox="0 0 10 10"><path d="M3 1l4 4-4 4" stroke="#fff" fill="none"/></svg></span>
  </div>
  <footer class="site-footer">
    <div class="follow">Follow Us <span class="social"></span><span class="social"></span><span class="social"></span><span class="social"></span></div>
    <div class="scroll">Scroll Down</div>
    <div class="footer-contact">Contact Us</div>
  </footer>
</section>

<!-- Our Difference -->
<section class="screen screen--difference">
  <div class="photo photo--team" role="img" aria-label="Photo of three colleagues working together at a table"></div>
  <header class="site-header">
    <div class="brand">TOLVANE</div>
    <div class="header-tools">
      <span class="phone"><svg width="8" height="8" viewBox="0 0 24 24"><path fill="#fff" d="M6.6 10.8a15 15 0 0 0 6.6 6.6l2.2-2.2a1 1 0 0 1 1-.25 11.4 11.4 0 0 0 3.6.6 1 1 0 0 1 1 1V20a1 1 0 0 1-1 1A17 17 0 0 1 3 4a1 1 0 0 1 1-1h3.5a1 1 0 0 1 1 1c0 1.25.2 2.45.6 3.6a1 1 0 0 1-.25 1z"/></svg>+1-202-555-0148</span>
      <span class="btn-contact">Contact Us</span>
      <span class="burger"><span></span><span></span><span></span></span>
    </div>
  </header>
  <div class="hero">
    <span class="tag">Our Difference</span>
    <h2 class="hero-title hero-title--mid">Why Tolvane</h2>
    <p class="hero-text">Lorem Ipsum is simply dummy text of the printing and typesetting industry. Lorem Ipsum has been the industry's standard dummy text ever printing and typesetting industry.</p>
    <span class="btn-outline">Learn More <svg width="8" height="8" viewBox="0 0 10 10"><path d="M2 8 8 2M4 2h4v4" stroke="#fff" fill="none"/></svg></span>
  </div>
  <footer class="site-footer">
    <div class="follow">Follow Us <span class="social"></span><span class="social"></span><span class="social"></span><span class="social"></span></div>
    <div class="scroll">Scroll Down</div>
    <div class="footer-contact">Contact Us</div>
  </footer>
</section>

<!-- Resources / blog post -->
<section class="screen screen--blog">
  <div class="photo photo--reader" role="img" aria-label="Photo of a businessman reading a newspaper with a coffee cup"></div>
  <header class="site-header">
    <div class="brand">TOLVANE</div>
    <div class="header-tools">
      <span class="burger"><span></span><span></span><span></span></span>
    </div>
  </header>
  <div class="hero">
    <span class="tag">Resources</span>
    <h2 class="hero-title hero-title--post">Behind the scenes<br>Of a very corvathicket<br>christmas</h2>
    <p class="byline">By: Ada Ferron &nbsp;|&nbsp; 31 Aug 2017</p>
    <span class="btn-outline">Read More <svg width="8" height="8" viewBox="0 0 10 10"><path d="M2 8 8 2M4 2h4v4" stroke="#fff" fill="none"/></svg></span>
  </div>
  <footer class="site-footer">
    <div class="follow">Follow Us <span class="social"></span><span class="social"></span><span class="social"></span><span class="social"></span></div>
    <div class="scroll">Scroll Up</div>
    <div class="footer-contact">Contact Us</div>
  </footer>
</section>

<!-- Home with menu open -->
<section class="screen screen--menu-open">
  <div class="photo photo--meeting" role="img" aria-label="Photo of colleagues in a business meeting"></div>
  <header class="site-header" style="right:262px">
    <div class="brand">TOLVANE</div>
    <div class="header-tools">
      <span class="phone"><svg width="8" height="8" viewBox="0 0 24 24"><path fill="#fff" d="M6.6 10.8a15 15 0 0 0 6.6 6.6l2.2-2.2a1 1 0 0 1 1-.25 11.4 11.4 0 0 0 3.6.6 1 1 0 0 1 1 1V20a1 1 0 0 1-1 1A17 17 0 0 1 3 4a1 1 0 0 1 1-1h3.5a1 1 0 0 1 1 1c0 1.25.2 2.45.6 3.6a1 1 0 0 1-.25 1z"/></svg>+1-202-555-0148</span>
      <span class="btn-contact">Contact Us</span>
    </div>
  </header>
  <div class="hero">
    <h1 class="hero-title">Welcome to<br>Tolvane</h1>
    <p class="hero-text">Lorem Ipsum is simply dummy text of the printing and typesetting industry. Lorem Ipsum has been the industry's standard dummy text ever printing and typesetting industry.</p>
    <span class="btn-outline">About Us <svg width="8" height="8" viewBox="0 0 10 10"><path d="M2 8 8 2M4 2h4v4" stroke="#fff" fill="none"/></svg></span>
  </div>
  <footer class="site-footer" style="right:262px">
    <div class="follow">Follow Us <span class="social"></span><span class="social"></span><span class="social"></span><span class="social"></span></div>
    <div class="scroll">Scroll Down</div>
  </footer>
  <nav class="menu-panel">
    <span class="menu-close">×</span>
    <ul class="menu-list">
      <li>Home</li>
      <li>Our Story</li>
      <li>Services</li>
      <li>Our Difference</li>
      <li class="current">Resources
        <ul class="submenu">
          <li>- Articles</li>
          <li class="active">- Blog</li>
          <li>- White Paper</li>
        </ul>
      </li>
      <li>Contact</li>
    </ul>
  </nav>
</section>

</body>
</html>
```